Selvin: A Friday night in the Prophetic Flyer

We are holding 2 Friday night events, one on 10/25/19 and the other on 11/29/19.
The time frame is 6:30pm-9:00pm. These services will be a time of prayer/healing for the sick and will be prophetic as well. (There will be prophets prophesying over people)

The event is called: Selvin: A Friday night in the Prophetic
The flyer should also include the phrase/excerpt: "And they prophesied also".

Keywords/Phrases: Prophetic, Healing, Climbing in the Spirit, Higher level of Anointing...

Target Market(s)

those looking for healing, seeking a word from God

Colors

Designer to choose colors to be used in the design.

Requirements
Must have
• The event is called: Selvin: A Friday night in the Prophetic
• The flyer should also include the phrase/excerpt: "And they prophesied also".
• It must include the Tovik logo attached, either is fine, we have attached two different versions.
• It must have the dates, location, time
• Dates: October 25, 2019 and November 29, 2019
• Location: Hollard Community Center
• (Downtown Portland) 482 Wendle Street
• Portland, ME 04102
• Time: 6:30pm-9:00pm
• Contact Info: Tel. 207-555-3841
• email: contact@brimfield-hall.org
• web: www.tovik.org
Nice to have
• creativity in color scheme, the meaning of the word Selvin conveyed in a classy artistic way/design.
Should not have
• Crosses, pictures of churches

```html
<!DOCTYPE html>
<html lang="en">
<head>
<meta charset="utf-8">
<title>Selvin: A Friday night in the Prophetic</title>
<link rel="stylesheet" href="https://fonts.googleapis.com/css2?family=Cinzel:wght@500;600&family=Cormorant+Garamond:wght@500;600;700&family=Montserrat:wght@700&family=Cabin:wght@500&display=swap">
<style>
  :root {
    --navy: #143d63;
    --navy-deep: #0f3657;
    --ink: #1c1c1c;
    --paper: #fdfbf1;
    --white: #ffffff;
  }
  html, body {
    margin: 0;
    padding: 0;
    overflow: hidden;
    background: var(--paper);
  }
  .flyer {
    position: relative;
    width: 927px;
    height: 1200px;
    overflow: hidden;
    background: var(--paper);
    font-family: "Cabin", sans-serif;
  }
  .artwork {
    position: absolute;
    inset: 0;
    background:
      radial-gradient(ellipse 260px 360px at 0% 18%, rgba(240,140,120,0.55), transparent 70%),
      radial-gradient(ellipse 260px 360px at 100% 18%, rgba(240,140,120,0.55), transparent 70%),
      radial-gradient(ellipse 220px 260px at 4% 48%, rgba(236,160,110,0.45), transparent 70%),
      radial-gradient(ellipse 220px 260px at 96% 48%, rgba(236,160,110,0.45), transparent 70%),
      radial-gradient(ellipse 300px 200px at 10% 100%, rgba(170,90,140,0.5), transparent 70%),
      radial-gradient(ellipse 300px 220px at 88% 92%, rgba(170,90,140,0.5), transparent 70%),
      radial-gradient(ellipse 420px 520px at 50% 55%, rgba(248,236,180,0.85), transparent 75%),
      linear-gradient(180deg, #fbf7ee 0%, #fbf3d4 55%, #f8efc2 80%, #fbf4dc 100%);
  }
  .title {
    position: absolute;
    top: 40px;
    left: 0;
    width: 100%;
    margin: 0;
    text-align: center;
    font-family: "Cinzel", serif;
    font-weight: 600;
    font-size: 86px;
    letter-spacing: 2px;
    line-height: 1;
    color: var(--navy);
  }
  .subtitle {
    position: absolute;
    top: 140px;
    left: 0;
    width: 100%;
    margin: 0;
    text-align: center;
    font-family: "Cormorant Garamond", serif;
    font-weight: 700;
    font-size: 44px;
    line-height: 1;
    color: var(--ink);
  }
  .ring-art {
    position: absolute;
    left: 322px;
    top: 222px;
    width: 300px;
    height: 306px;
    border-radius: 50%;
    background: radial-gradient(circle at 50% 45%, rgba(240,150,80,0.45) 55%, rgba(200,110,150,0.35) 78%, transparent 100%);
  }
  .quote-disc {
    position: absolute;
    left: 363px;
    top: 282px;
    width: 206px;
    height: 206px;
    border-radius: 50%;
    background: var(--navy-deep);
  }
  .quote {
    position: absolute;
    left: 370px;
    top: 324px;
    width: 192px;
    margin: 0;
    text-align: center;
    font-family: "Cormorant Garamond", serif;
    font-weight: 600;
    font-variant: small-caps;
    font-size: 31px;
    line-height: 37px;
    letter-spacing: 0.5px;
    color: var(--white);
  }
  .schedule {
    position: absolute;
    top: 566px;
    left: 0;
    width: 100%;
    text-align: center;
    font-family: "Montserrat", sans-serif;
    font-weight: 700;
    font-size: 28px;
    line-height: 36px;
    color: var(--navy);
  }
  .schedule p { margin: 0; }
  .venue {
    position: absolute;
    top: 664px;
    left: 0;
    width: 100%;
    margin: 0;
    text-align: center;
    font-style: normal;
    font-family: "Cabin", sans-serif;
    font-weight: 500;
    font-size: 35px;
    line-height: 38px;
    color: var(--ink);
  }
  .contact {
    position: absolute;
    top: 860px;
    left: 0;
    width: 100%;
    margin: 0;
    text-align: center;
    font-style: normal;
    font-family: "Cormorant Garamond", serif;
    font-weight: 600;
    font-size: 21px;
    line-height: 25px;
    color: var(--ink);
  }
  .contact .phone-icon {
    display: inline-block;
    width: 17px;
    height: 17px;
    vertical-align: -2px;
    margin: 0 5px 0 7px;
  }
  .brand-mark {
    position: absolute;
    left: 367px;
    top: 967px;
    width: 192px;
    height: 192px;
    background: var(--navy-deep);
    display: flex;
    align-items: center;
    justify-content: center;
  }
  .brand-name {
    font-family: "Cinzel", serif;
    font-weight: 500;
    font-size: 44px;
    color: var(--white);
    letter-spacing: 1px;
  }
</style>
</head>
<body>
<main class="flyer">
  <div class="artwork" role="img" aria-label="Soft watercolour tree with pink, orange and plum autumn leaves"></div>

  <h1 class="title">SELVIN:</h1>
  <p class="subtitle">A Friday night in the Prophetic</p>

  <div class="ring-art" role="img" aria-label="Ring of rainbow-coloured dots circling the quote"></div>
  <div class="quote-disc"></div>
  <p class="quote">“And they prophesied also.”</p>

  <div class="schedule">
    <p>OCTOBER 25, 2019 &amp; NOVEMBER 29, 2019</p>
    <p>6:30pm-9:00pm</p>
  </div>

  <address class="venue">
    Hollard Community Center<br>
    (Downtown Portland)<br>
    482 Wendle Street<br>
    Portland, ME 04102
  </address>

  <address class="contact">
    For details, contact:<svg class="phone-icon" viewBox="0 0 16 16" aria-hidden="true"><path d="M4 1.5 6 4.5 4.8 6.2c.8 1.8 2.2 3.2 4 4L10.5 9l3 2-1.2 2.6C7.5 13.7 2.3 8.5 2.4 3.7Z" fill="none" stroke="#1c1c1c" stroke-width="1.2" stroke-linejoin="round"/></svg>207-555-3841<br>
    email: contact@brimfield-hall.org<br>
    web: www.tovik.org
  </address>

  <div class="brand-mark">
    <span class="brand-name">TOVIK</span>
  </div>
</main>
</body>
</html>
```